Mainpage design for a catalog service
Designers,
We are trying our level best to get in contact with the client and get this project finalized as soon as possible.
Any further updates will be posted on the contest page.
Thank you!
please extend contest
To designers:
The ads on the left and right are not fixed size ads. They may vary in size and shape. If you take a look at the attached picture for kvelma.no you will notice that the actual ad is defined in the background and it takes up all the available space.
RK/PTF/HW Team
Please feel free to use free pictures which are available on the internet in the design. Preferably we want a design with least amount of pictures.
We are looking for simplify and to make a fresher design for the site. The ads on the left and right are floating on the background. You are free to be creative for these ads. they don't need to be aligned vertically with the design or to be constraint to the given space in the prototype picture

```html
<!DOCTYPE html>
<html lang="en">
<head>
<meta charset="utf-8">
<title>dolvask – Find Locations &amp; Contact Information</title>
<link rel="stylesheet" href="https://fonts.googleapis.com/css2?family=Arimo:wght@400;700&family=Libre+Baskerville:ital,wght@0,700;1,400;1,700&display=swap">
<style>
  :root {
    --page-bg: #ffffff;
    --green-dark: #1f4d0c;
    --green-mid: #3f7d14;
    --green-light: #6fae2a;
    --green-text: #2f7a12;
    --red: #e0141b;
    --ink: #222222;
    --chip-bg: #f3f3f3;
    --chip-border: #b9c9ad;
    --white: #ffffff;
  }
  * { box-sizing: border-box; margin: 0; padding: 0; }
  html, body { width: 1200px; height: 766px; overflow: hidden; background: var(--page-bg); }
  body { position: relative; font-family: "Arimo", Arial, sans-serif; color: var(--ink); }

  /* Top banner */
  .top-banner {
    position: absolute; left: 264px; top: 10px; width: 672px; height: 162px;
    background: linear-gradient(#ffffff, #ececec); border: 1px solid #dcdcdc;
  }
  .top-banner .magnifier-art {
    position: absolute; left: 28px; top: 12px; width: 110px; height: 135px;
    background: radial-gradient(circle at 50% 40%, #d6d6d6, #9a9a9a); border-radius: 40px;
  }
  .top-banner .mini-art {
    position: absolute; right: 22px; top: 92px; width: 46px; height: 50px;
    background: radial-gradient(circle, #dedede, #a9a9a9); border-radius: 18px;
  }
  .top-banner .headline {
    position: absolute; left: 156px; top: 20px; width: 300px; text-align: center;
    font-family: "Libre Baskerville", Georgia, serif; font-weight: 700; font-size: 32px; color: var(--red);
  }
  .top-banner .subhead {
    position: absolute; left: 176px; top: 66px; width: 440px; text-align: center;
    font-weight: 700; font-size: 24px; color: var(--ink);
  }
  .top-banner .blurb {
    position: absolute; left: 206px; top: 100px; width: 384px; text-align: center;
    font-size: 11.5px; line-height: 1.4; color: #444;
  }
  .top-banner .cta {
    position: absolute; left: 206px; top: 139px; width: 384px; text-align: center;
    font-size: 11px; font-weight: 700; color: var(--ink);
  }

  /* Side ads */
  .side-ad { position: absolute; top: 226px; width: 264px; }
  .side-ad.left { left: 0; }
  .side-ad.right { left: 936px; }
  .side-ad .ad-copy {
    width: 214px; margin: 0 auto; height: 152px;
    font-family: "Libre Baskerville", Georgia, serif; font-style: italic; font-size: 12.5px;
    line-height: 1.55; color: var(--green-text); text-align: center;
  }
  .side-ad .ad-art {
    width: 264px; height: 222px;
    background: radial-gradient(ellipse at 50% 55%, #f2d34a 0 16%, #cfd5d8 17%, #e8ecef 55%, #ffffff 78%);
  }
  .side-ad .ad-title {
    margin-top: 20px; text-align: center; font-family: "Libre Baskerville", Georgia, serif;
    font-style: italic; font-weight: 700; font-size: 25px; color: var(--green-text);
  }

  /* Main panel */
  .main-panel {
    position: absolute; left: 264px; top: 180px; width: 672px; height: 548px;
    background: linear-gradient(180deg, var(--green-mid) 0%, var(--green-light) 30%, var(--green-mid) 60%, var(--green-dark) 100%);
    border-radius: 10px; box-shadow: 0 4px 14px rgba(0,0,0,.35); overflow: hidden;
  }
  .panel-header { position: absolute; left: 0; top: 0; width: 100%; height: 180px;
    background: linear-gradient(180deg, #2f6610, #4d9118 60%, rgba(0,0,0,0)); }
  .brand { position: absolute; left: 20px; top: 22px; width: 140px; text-align: center; }
  .brand-mark {
    width: 84px; height: 84px; margin: 0 auto; border-radius: 50%;
    background: radial-gradient(circle at 40% 35%, #7fcf34, #2d6b0c); border: 3px solid #cfe9b6;
  }
  .brand-name { margin-top: 8px; font-size: 28px; color: var(--white); letter-spacing: 1px; }
  .search-title {
    position: absolute; left: 226px; top: 38px; font-style: italic; font-size: 16px; color: var(--white);
  }
  .search-bar {
    position: absolute; left: 218px; top: 70px; width: 392px; height: 50px;
    background: linear-gradient(#f7f7f7, #d9d9d9); border-radius: 4px; border: 1px solid #9dbb86;
  }
  .search-field {
    position: absolute; left: 10px; top: 10px; width: 320px; height: 30px;
    background: #bdbdbd; border-radius: 4px; color: var(--white); font-size: 12px; padding: 8px 10px;
    white-space: nowrap; overflow: hidden;
  }
  .search-bar svg { position: absolute; right: 10px; top: 6px; }

  .categories-label { position: absolute; left: 14px; top: 222px; font-size: 20px; color: var(--white); }
  .category-grid {
    position: absolute; left: 16px; top: 252px; width: 640px;
    display: grid; grid-template-columns: repeat(4, 148px); column-gap: 16px; row-gap: 5px;
  }
  .category-item {
    height: 14px; background: var(--chip-bg); border: 1px solid var(--chip-border); border-radius: 3px;
    font-size: 8px; line-height: 12px; color: #555; padding-left: 6px; white-space: nowrap; overflow: hidden;
  }
  .category-item.active { background: #d8ef9a; }

  .footer-nav {
    position: absolute; left: 0; top: 490px; width: 100%; text-align: center; font-size: 10px; color: #e7f3da;
  }
  .footer-nav a { color: inherit; text-decoration: none; margin: 0 8px; }
  .footer-nav a.current { color: #fff59a; }
  .footer-rule { position: absolute; left: 220px; top: 510px; width: 232px; height: 1px; background: rgba(255,255,255,.4); }
  .copyright {
    position: absolute; left: 0; top: 528px; width: 100%; text-align: center; font-size: 9px; color: #cfe3bd;
  }
</style>
</head>
<body>
  <header class="top-banner">
    <div class="magnifier-art" role="img" aria-label="Illustrated figure holding a magnifying glass"></div>
    <div class="headline">IF YOU WANT !</div>
    <div class="subhead">FIND YOUR CONTACT INFORMATION</div>
    <p class="blurb">The company is a business catalog service providing their customers with business contact information and locations</p>
    <div class="cta">CLICK HERE</div>
    <div class="mini-art" role="img" aria-label="Small illustrated figure with magnifier"></div>
  </header>

  <aside class="side-ad left">
    <p class="ad-copy">Lorem Ipsum is simply dummy text of the printing and typesetting industry. Lorem Ipsum has been the industry's standard dummy text ever since the 1500s, when an</p>
    <div class="ad-art" role="img" aria-label="Sketched city landmarks, a yellow folder and a hand holding the panel edge"></div>
    <div class="ad-title">Find Location</div>
  </aside>
  <aside class="side-ad right">
    <p class="ad-copy">Lorem Ipsum is simply dummy text of the printing and typesetting industry. Lorem Ipsum has been the industry's standard dummy text ever since the 1500s, when an</p>
    <div class="ad-art" role="img" aria-label="Sketched city landmarks, a yellow folder and a hand holding the panel edge"></div>
    <div class="ad-title">Find Location</div>
  </aside>

  <main class="main-panel">
    <div class="panel-header"></div>
    <div class="brand">
      <div class="brand-mark"></div>
      <div class="brand-name">dolvask</div>
    </div>
    <div class="search-title">Find Locations &amp; Contact Information</div>
    <div class="search-bar">
      <div class="search-field">Search Contact Information and Locations</div>
      <svg width="40" height="38" viewBox="0 0 40 38" aria-hidden="true">
        <path d="M4 20 L15 31 L36 6" fill="none" stroke="#2f7a12" stroke-width="7" stroke-linecap="round" stroke-linejoin="round"/>
      </svg>
    </div>

    <div class="categories-label">Categories:</div>
    <div class="category-grid">
      <div class="category-item active">Lorem Ipsum is simply dummy</div><div class="category-item">Lorem Ipsum is simply dummy</div><div class="category-item">Lorem Ipsum is simply dummy</div><div class="category-item">Lorem Ipsum is simply dummy</div>
      <div class="category-item">Lorem Ipsum is simply dummy</div><div class="category-item">Lorem Ipsum is simply dummy</div><div class="category-item">Lorem Ipsum is simply dummy</div><div class="category-item">Lorem Ipsum is simply dummy</div>
      <div class="category-item">Lorem Ipsum is simply dummy</div><div class="category-item">Lorem Ipsum is simply dummy</div><div class="category-item">Lorem Ipsum is simply dummy</div><div class="category-item">Lorem Ipsum is simply dummy</div>
      <div class="category-item">Lorem Ipsum is simply dummy</div><div class="category-item">Lorem Ipsum is simply dummy</div><div class="category-item">Lorem Ipsum is simply dummy</div><div class="category-item">Lorem Ipsum is simply dummy</div>
      <div class="category-item">Lorem Ipsum is simply dummy</div><div class="category-item">Lorem Ipsum is simply dummy</div><div class="category-item">Lorem Ipsum is simply dummy</div><div class="category-item">Lorem Ipsum is simply dummy</div>
      <div class="category-item">Lorem Ipsum is simply dummy</div><div class="category-item">Lorem Ipsum is simply dummy</div><div class="category-item">Lorem Ipsum is simply dummy</div><div class="category-item">Lorem Ipsum is simply dummy</div>
      <div class="category-item">Lorem Ipsum is simply dummy</div><div class="category-item">Lorem Ipsum is simply dummy</div><div class="category-item">Lorem Ipsum is simply dummy</div><div class="category-item">Lorem Ipsum is simply dummy</div>
      <div class="category-item">Lorem Ipsum is simply dummy</div><div class="category-item">Lorem Ipsum is simply dummy</div><div class="category-item">Lorem Ipsum is simply dummy</div><div class="category-item">Lorem Ipsum is simply dummy</div>
    </div>

    <nav class="footer-nav">
      <a class="current" href="#">Home</a> | <a href="#">Services</a> | <a href="#">About Us</a> | <a href="#">Contact Us</a>
    </nav>
    <div class="footer-rule"></div>
    <div class="copyright">© 2011 www.dolvask.no. All Rights Reserved</div>
  </main>
</body>
</html>
```